Re-Design Business Card and Logo for Plastic Printing

Business is a small financial planning (investments, insurance, retirement, etc.) firm. The majority of our clients are 55+ years old, professional occupations (pilots, doctors, bankers, etc.) but not necessarily "high net worth."
I would like to have a design that would be used on clear plastic business cards. I have found a vendor that makes these but I do not have the ability to design these like I want.
I do have one proof but I just don't feel like it's the right one for me. Also, I feel that I need some help with a logo redesign so maybe someone could handle that for me as well.
I want the final design to "eye catching" but still be tasteful. I am open to suggestion regarding colors and such.
I will include the old design as well as the new proof I have to give you an idea of what I current have. Keep in mind, I have no allegiance to the attached designs.
For the second file (Business Card New Proof), the white space shown will be transparent when printed on plastic card.
Target Market(s)
Mostly people age 55+ in professional occupations.
Industry/Entity Type
Financial Service
Contact Information for Business Card
Looking for design that can be printed on clear plastic cards (if possible).
Logo Text
HWC - Harborline Wealth Counsel
Requirements
Must have
- Must be double sided because disclosure is required for compliance reasons.
Designations (must include the Registered trademark symbol as follows)...
MBA, ChFC®, CLU®, CRPS®
Nice to have
- The little icons next to email, phone and fax are nice.
Should not have
- I think I would like to eliminate the Owner and Co-Founder line that you see on the attachments.

```html
<!DOCTYPE html>
<html lang="en">
<head>
<meta charset="utf-8">
<title>Harborline Wealth Counsel – Business Card</title>
<link href="https://fonts.googleapis.com/css2?family=Montserrat:wght@400;500;700&family=Roboto+Condensed:wght@400;700&display=swap" rel="stylesheet">
<style>
  :root {
    --bg: #dcdfe0;
    --card: rgba(255, 255, 255, 0.55);
    --card-edge: rgba(255, 255, 255, 0.9);
    --navy: #163a66;
    --blue: #0b5a86;
    --blue-deep: #0a4a75;
    --steel: #7d8e99;
    --ink: #2c3338;
    --muted: #6a7379;
    --white: #ffffff;
  }
  * { box-sizing: border-box; margin: 0; padding: 0; }
  html, body { width: 1200px; height: 927px; overflow: hidden; }
  body {
    background: var(--bg);
    font-family: "Montserrat", Arial, sans-serif;
    position: relative;
  }
  .card {
    position: absolute;
    left: 270px;
    width: 660px;
    height: 380px;
    background: var(--card);
    border: 1.5px solid var(--card-edge);
    border-radius: 6px;
    overflow: hidden;
    box-shadow: 0 10px 30px rgba(40, 55, 65, 0.12);
  }
  .card--disclosure { top: 56px; }
  .card--contact { top: 490px; }

  .brand {
    position: absolute;
    text-align: center;
    color: var(--navy);
    font-family: "Montserrat", Arial, sans-serif;
    font-weight: 700;
    text-transform: uppercase;
    line-height: 1.2;
  }
  .brand__dot {
    display: block;
    margin: 0 auto 12px;
    width: 54px; height: 54px;
    border-radius: 50%;
    background: var(--navy);
  }
  .card--disclosure .brand { left: 0; right: 0; top: 40px; font-size: 22px; letter-spacing: 1px; }
  .card--contact .brand { right: 30px; top: 70px; width: 300px; font-size: 17px; letter-spacing: 0.5px; }

  .band { position: absolute; left: 0; top: 190px; width: 660px; height: 40px; }

  .disclosure {
    position: absolute;
    left: 60px; right: 60px; top: 258px;
    font-size: 12px;
    line-height: 1.55;
    color: var(--muted);
    font-weight: 400;
  }

  .person { position: absolute; left: 44px; top: 42px; }
  .person__name {
    font-family: "Roboto Condensed", Arial, sans-serif;
    font-weight: 700;
    font-size: 50px;
    letter-spacing: 0.5px;
    color: var(--blue);
    line-height: 1;
  }
  .person__credentials {
    margin-top: 10px;
    font-size: 21px;
    color: var(--muted);
    font-weight: 500;
  }

  .contact-panel { position: absolute; left: 0; bottom: 0; width: 400px; height: 146px; }
  .contact-list {
    position: absolute;
    left: 46px; bottom: 22px;
    list-style: none;
    font-family: "Roboto Condensed", Arial, sans-serif;
    color: var(--white);
    font-size: 17px;
  }
  .contact-list li { display: flex; align-items: center; gap: 10px; margin-top: 8px; }
  .contact-list li:first-child { font-weight: 700; font-size: 19px; margin-bottom: 6px; }
  .contact-list svg { width: 15px; height: 15px; flex: none; }

  .address {
    position: absolute;
    right: 36px; bottom: 70px;
    display: flex; gap: 10px; align-items: flex-start;
    font-family: "Roboto Condensed", Arial, sans-serif;
    font-style: normal;
    font-size: 19px;
    color: var(--ink);
    line-height: 1.3;
  }
  .address svg { width: 16px; height: 16px; margin-top: 4px; flex: none; }
</style>
</head>
<body>

<section class="card card--disclosure" aria-label="Card back: disclosure">
  <div class="brand">
    <span class="brand__dot"></span>
    HWC<br>Harborline Wealth Counsel
  </div>
  <svg class="band" viewBox="0 0 660 40" preserveAspectRatio="none" aria-hidden="true">
    <defs>
      <linearGradient id="bandGrad" x1="0" x2="1">
        <stop offset="0" stop-color="#0a4a75"/>
        <stop offset="1" stop-color="#0b5a86"/>
      </linearGradient>
    </defs>
    <polygon points="0,6 150,6 140,34 0,34" fill="#7d8e99" opacity="0.75"/>
    <polygon points="162,6 660,6 660,34 152,34" fill="url(#bandGrad)"/>
  </svg>
  <p class="disclosure">
    Mark Ellison is a registered representative of and offers securities and investment advisory services through Northgate Securities Corporation, member FINRA/SIPC. Northgate Securities Corporation is a member of Northgate Financial Group, which is the marketing name for Northgate Corporation and its affiliates.
  </p>
</section>

<section class="card card--contact" aria-label="Card front: contact details">
  <div class="person">
    <h1 class="person__name">MARK ELLISON</h1>
    <p class="person__credentials">MBA, ChFC®, CLU®, CRPS®</p>
  </div>

  <svg class="contact-panel" viewBox="0 0 440 146" preserveAspectRatio="none" aria-hidden="true">
    <defs>
      <linearGradient id="panelGrad" x1="0" x2="1" y1="0" y2="1">
        <stop offset="0" stop-color="#0b5a86"/>
        <stop offset="1" stop-color="#0a4a75"/>
      </linearGradient>
    </defs>
    <path d="M0,0 H330 Q352,0 362,18 L440,146 H0 Z" fill="url(#panelGrad)"/>
  </svg>

  <ul class="contact-list">
    <li>
      <svg viewBox="0 0 16 16" aria-hidden="true"><circle cx="8" cy="8" r="8" fill="#fff"/><path d="M5 4.5l1.6-.3.8 2-1 .8a5 5 0 0 0 2.6 2.6l.8-1 2 .8-.3 1.6c-3.6.2-6.7-2.9-6.5-6.5z" fill="#0b5a86"/></svg>
      (555) 214-0183
    </li>
    <li>
      <svg viewBox="0 0 16 16" aria-hidden="true"><circle cx="8" cy="8" r="8" fill="#fff"/><rect x="4" y="5.2" width="8" height="5.6" rx="0.6" fill="none" stroke="#0b5a86" stroke-width="1.1"/><path d="M4.2 5.6L8 8.4l3.8-2.8" fill="none" stroke="#0b5a86" stroke-width="1.1"/></svg>
      mellison@harborlinewc.com
    </li>
    <li>
      <svg viewBox="0 0 16 16" aria-hidden="true"><circle cx="8" cy="8" r="8" fill="#fff"/><circle cx="8" cy="8" r="4" fill="none" stroke="#0b5a86" stroke-width="1.1"/><path d="M4 8h8M8 4c-2 2.4-2 5.6 0 8M8 4c2 2.4 2 5.6 0 8" fill="none" stroke="#0b5a86" stroke-width="0.9"/></svg>
      Toll Free (555) 300-4718
    </li>
  </ul>

  <div class="brand">
    <span class="brand__dot"></span>
    HWC<br>Harborline Wealth Counsel
  </div>

  <address class="address">
    <svg viewBox="0 0 16 16" aria-hidden="true"><circle cx="8" cy="8" r="8" fill="#2c3338"/><circle cx="8" cy="7" r="2.3" fill="#fff"/></svg>
    <span>1180 Tidewater Ave, Suite 310<br>Norfield, VA 23999</span>
  </address>
</section>

</body>
</html>
```